Flyer/Brochure for Product & Services Bundles

Create a single-page PDF to help market our new product & service bundles. Use the colors as noted in attachment. I can provide text and concepts later.

Industry/Entity Type

Laboratory Instruments

Colors
0054AA
0677BA
7BADD7
CADEEF
E8F1F8
59FF00
82FF00
B8FF75
E3FFCB
F4FFEA

```html
<!DOCTYPE html>
<html lang="en">
<head>
<meta charset="utf-8">
<title>Vireo Scientific – Complete Laboratory Solutions</title>
<link href="https://fonts.googleapis.com/css2?family=Poppins:wght@400;600&family=Roboto:wght@400;500;700&display=swap" rel="stylesheet">
<style>
  :root {
    --navy: #1f4f9e;
    --ink: #1a1a1a;
    --green: #8cc63f;
    --sky: #cadeef;
    --mist: #e8f1f8;
    --footer: #3a5f96;
    --white: #ffffff;
  }
  * { margin: 0; padding: 0; box-sizing: border-box; }
  html, body { width: 762px; height: 1200px; overflow: hidden; background: var(--white); }
  .flyer { position: relative; width: 762px; height: 1200px; overflow: hidden; font-family: "Roboto", Arial, sans-serif; color: var(--ink); }
  .backdrop { position: absolute; inset: 0; }
  .brand { position: absolute; top: 50px; left: 0; width: 762px; display: flex; justify-content: center; align-items: center; gap: 12px; }
  .brand-dot { width: 26px; height: 26px; border-radius: 50%; background: var(--green); }
  .brand-name { font-family: "Poppins", sans-serif; font-weight: 600; font-size: 30px; color: var(--navy); }
  .headline { position: absolute; top: 166px; width: 100%; text-align: center; font-family: "Poppins", sans-serif; font-weight: 600; font-size: 31px; color: var(--navy); letter-spacing: -0.3px; }
  .subline { position: absolute; top: 210px; width: 100%; text-align: center; font-family: "Poppins", sans-serif; font-size: 19px; color: var(--ink); }
  .frame { position: absolute; border: 3px solid var(--green); }
  .product-photo { position: absolute; border-radius: 8px; background: linear-gradient(135deg, #f2f4f7 0%, #d9dee6 45%, #2f4fa0 75%, #e9ecf1 100%); box-shadow: 0 6px 14px rgba(0,0,0,0.15); }
  .product-photo.sampler { background: linear-gradient(160deg, #2a2a2e 0%, #3a3b40 45%, #f1f3f6 55%, #e3e7ee 80%, #2b4f9c 86%, #f1f3f6 92%); }
  .label { position: absolute; font-weight: 700; font-size: 17.5px; color: var(--navy); letter-spacing: -0.6px; white-space: nowrap; }
  .feature { position: absolute; top: 798px; width: 210px; text-align: center; }
  .feature-icon { width: 55px; height: 55px; border-radius: 50%; background: var(--green); margin: 0 auto; display: flex; align-items: center; justify-content: center; }
  .feature-title { margin-top: 11px; font-weight: 700; font-size: 20px; color: var(--navy); }
  .feature-text { margin-top: 6px; font-size: 15.5px; line-height: 19px; color: var(--ink); }
  .cta { position: absolute; left: 190px; top: 984px; width: 382px; height: 55px; border-radius: 28px; background: var(--green); color: var(--white); font-weight: 700; font-size: 21px; display: flex; align-items: center; justify-content: center; letter-spacing: 0.2px; }
  .contact-band { position: absolute; left: 0; top: 1081px; width: 762px; height: 119px; background: var(--footer); color: var(--white); }
  .contact-title { position: absolute; top: 18px; width: 100%; text-align: center; font-family: "Poppins", sans-serif; font-size: 21px; }
  .contact-line { position: absolute; top: 71px; width: 100%; display: flex; justify-content: center; align-items: center; gap: 14px; font-family: "Poppins", sans-serif; font-size: 17px; font-weight: 400; }
  .divider { width: 2px; height: 24px; background: var(--white); }
</style>
</head>
<body>
<main class="flyer">
  <svg class="backdrop" width="762" height="1200" viewBox="0 0 762 1200" aria-hidden="true">
    <defs>
      <linearGradient id="wash" x1="0" y1="0" x2="1" y2="1">
        <stop offset="0" stop-color="#e8f1f8"/>
        <stop offset="1" stop-color="#b9d6ee"/>
      </linearGradient>
    </defs>
    <polygon points="762,120 762,700 420,560" fill="#e8f1f8"/>
    <polygon points="0,310 300,430 0,530" fill="url(#wash)" opacity="0.8"/>
    <polygon points="0,530 762,470 762,680 360,505" fill="#cadeef" opacity="0.7"/>
    <polygon points="0,840 360,505 0,600" fill="#e8f1f8"/>
    <polygon points="560,560 762,600 762,680" fill="#a9cbe8" opacity="0.7"/>
  </svg>

  <header class="brand">
    <span class="brand-dot"></span>
    <span class="brand-name">Vireo Scientific</span>
  </header>

  <h1 class="headline">Complete Laboratory Solutions</h1>
  <p class="subline">Mercury Analyzers &amp; Auto Sample Changers</p>

  <div class="frame" style="left:137px;top:292px;width:221px;height:190px"></div>
  <div class="product-photo" role="img" aria-label="Mercury analyzer with reduction unit and laptop" style="left:92px;top:318px;width:322px;height:134px"></div>
  <p class="label" style="left:188px;top:494px">HX-300 SCR</p>

  <div class="frame" style="left:438px;top:290px;width:114px;height:184px"></div>
  <div class="product-photo" role="img" aria-label="Mercury analyzer unit" style="left:483px;top:308px;width:135px;height:140px"></div>
  <p class="label" style="left:571px;top:456px">HX-300</p>

  <div class="frame" style="left:128px;top:625px;width:221px;height:100px"></div>
  <div class="product-photo sampler" role="img" aria-label="Analyzer with auto sample changer" style="left:157px;top:552px;width:162px;height:136px"></div>
  <p class="label" style="left:146px;top:733px">QL - 700F + AUTOLIFT 3F</p>

  <div class="frame" style="left:399px;top:626px;width:238px;height:99px"></div>
  <div class="frame" style="left:461px;top:510px;width:176px;height:215px"></div>
  <div class="product-photo sampler" role="img" aria-label="Analyzer with auto sample changer" style="left:417px;top:544px;width:194px;height:140px"></div>
  <p class="label" style="left:440px;top:733px">QL - 700A + AUTOLIFT5</p>

  <section class="feature" style="left:46px">
    <div class="feature-icon">
      <svg width="34" height="34" viewBox="0 0 34 34" fill="none" stroke="#fff" stroke-width="2.2" aria-hidden="true">
        <circle cx="17" cy="17" r="5"/>
        <path d="M17 4v5M17 25v5M4 17h5M25 17h5M7.8 7.8l3.5 3.5M22.7 22.7l3.5 3.5M7.8 26.2l3.5-3.5M22.7 11.3l3.5-3.5"/>
        <circle cx="17" cy="17" r="10"/>
      </svg>
    </div>
    <h2 class="feature-title">High Throughput</h2>
    <p class="feature-text">Maximize productivity with rapid analysis and large sample capacity.</p>
  </section>

  <section class="feature" style="left:276px">
    <div class="feature-icon">
      <svg width="34" height="34" viewBox="0 0 34 34" fill="none" stroke="#fff" stroke-width="2.2" aria-hidden="true">
        <circle cx="16" cy="18" r="12"/><circle cx="16" cy="18" r="7"/><circle cx="16" cy="18" r="2"/>
        <path d="M16 18L29 5M24 5h5v5"/>
      </svg>
    </div>
    <h2 class="feature-title">Precision Analysis</h2>
    <p class="feature-text">Achieve accurate and reliable results for mercury measurement.</p>
  </section>

  <section class="feature" style="left:506px">
    <div class="feature-icon">
      <svg width="34" height="34" viewBox="0 0 34 34" fill="none" stroke="#fff" stroke-width="2.2" aria-hidden="true">
        <circle cx="17" cy="17" r="13"/><path d="M17 9v8l5 5"/>
      </svg>
    </div>
    <h2 class="feature-title">Automated Systems</h2>
    <p class="feature-text">Streamline workflows with seamless auto sample changer integration.</p>
  </section>

  <div class="cta">CONTACT FOR BUNDLE DETAILS</div>

  <footer class="contact-band">
    <p class="contact-title">Contact Us:</p>
    <p class="contact-line">
      <span>Phone: (555)987-6543</span><span class="divider"></span>
      <span>Email: info@vireolab.com</span><span class="divider"></span>
      <span>Web: www.vireolab.com</span>
    </p>
  </footer>
</main>
</body>
</html>
```